Need a redesign for our Wordpress Credit report website

Hi, We need someone to redesign our Wordpress credit report website, brightledgerview.co.za. The designer will be responsible for the following pages:
- home page
- blog page
- single post
- dashboard
- credit report page

About BrightLedgerView.co.za
Bright Ledger View is a consumer focussed credit report platform where South African citizens can get an easy to understand credit report that shows them where to improve their credit scores.

```html
<!DOCTYPE html>
<html lang="en">
<head>
<meta charset="utf-8">
<title>Bright Ledger View – Check your credit score</title>
<link href="https://fonts.googleapis.com/css2?family=Roboto:wght@400;500;700;900&family=Roboto+Condensed:wght@700&display=swap" rel="stylesheet">
<style>
:root{
  --blue:#1d5cb8;
  --blue-dark:#154a97;
  --green:#7cc242;
  --green-dark:#62a92c;
  --navy:#0d1c3a;
  --ink:#333a44;
  --muted:#7b838e;
  --light:#eef1f5;
  --grey:#f3f4f6;
  --line:#dfe3e8;
  --white:#ffffff;
  --footer-text:#dce6f5;
}
*{box-sizing:border-box;margin:0;padding:0}
html,body{width:1200px;height:3732px;overflow:hidden}
body{position:relative;font-family:"Roboto",sans-serif;color:var(--ink);background:var(--white);font-size:14px;line-height:1.5}
.abs{position:absolute}
/* header */
.site-header{left:0;top:0;width:1200px;height:80px;z-index:5}
.brand{left:32px;top:18px;display:flex;align-items:center;gap:10px}
.brand-dot{width:40px;height:40px;border-radius:50%;background:var(--blue)}
.brand-name{font-weight:700;font-size:20px;color:var(--blue)}
.main-nav{left:600px;top:34px;display:flex;gap:40px;font-size:13px;font-weight:700;color:var(--white);letter-spacing:.5px}
.main-nav .active{color:var(--blue)}
.btn-login{left:1000px;top:24px;width:104px;height:40px;border-radius:4px;background:var(--blue);color:var(--white);font-weight:700;font-size:13px;display:flex;align-items:center;justify-content:center}
/* hero */
.hero{left:0;top:0;width:1200px;height:620px;background:var(--light);overflow:hidden}
.hero-wave{left:0;top:0}
.hero-devices{left:140px;top:120px;width:420px;height:300px;border-radius:6px;background:linear-gradient(135deg,#dfe6ee,#b9c6d6 60%,#9fb0c4)}
.hero-title{left:88px;top:428px;font-family:"Roboto Condensed",sans-serif;font-weight:700;font-size:46px;line-height:1.08;color:var(--blue);letter-spacing:.5px}
.signup-card{left:760px;top:100px;width:400px;height:470px;background:var(--white);border-radius:6px;box-shadow:0 6px 24px rgba(20,40,80,.15);padding:26px 30px}
.signup-card h2{font-size:24px;font-weight:900;color:var(--green);text-align:center;margin-bottom:18px}
.field{height:42px;border:1px solid var(--line);border-radius:3px;margin-bottom:12px;padding:0 14px;display:flex;align-items:center;font-size:13px;color:var(--muted)}
.agree{display:flex;align-items:center;gap:10px;font-size:12px;color:var(--muted);margin:6px 0 16px}
.agree span{width:16px;height:16px;border:1px solid #b6bdc6;border-radius:2px}
.btn-submit{height:42px;border-radius:3px;background:var(--green);color:var(--white);font-weight:700;font-size:14px;display:flex;align-items:center;justify-content:center}
.signup-note{left:760px;top:580px;width:400px;font-size:12px;color:var(--muted);text-align:center;line-height:1.45;z-index:2}
/* benefit row */
.benefits{left:80px;top:680px;width:1040px;display:flex;justify-content:space-between}
.benefit{display:flex;gap:14px;width:240px;font-size:15px;color:var(--ink);line-height:1.35}
.tick{flex:none;width:32px;height:32px}
.rule{left:80px;top:770px;width:1040px;height:1px;background:var(--line)}
/* about */
.about-ring{left:90px;top:830px;width:300px;height:300px;border-radius:50%;border:10px solid var(--green)}
.about-photo{left:110px;top:850px;width:260px;height:260px;border-radius:50%;background:linear-gradient(135deg,#c9d3dc,#8e9fae 55%,#5d7082)}
.about-text{left:520px;top:850px;width:620px}
.section-title{font-weight:900;font-size:32px;color:var(--blue);letter-spacing:.5px}
.about-text .section-title{padding-bottom:10px;border-bottom:4px solid var(--green);display:inline-block;margin-bottom:22px}
.about-text p{font-size:15px;color:var(--ink);margin-bottom:18px;line-height:1.6}
.about-text a{color:var(--blue)}
/* system features */
.features{left:0;top:1200px;width:1200px;height:420px;background:var(--grey)}
.features-photo{left:660px;top:1200px;width:540px;height:420px;background:linear-gradient(135deg,#e6ebf0,#aab8c6 55%,#6d8197)}
.features-title{left:88px;top:1272px}
.features-title .section-title{padding-bottom:10px;border-bottom:4px solid var(--green)}
.feature-col{top:1348px;display:flex;flex-direction:column;gap:26px;width:250px}
.feature{display:flex;gap:14px;align-items:center;font-size:14px;line-height:1.35}
.f-icon{flex:none;width:44px;height:44px;border-radius:50%;background:var(--green);display:flex;align-items:center;justify-content:center}
/* headings with side rules */
.center-head{left:0;width:1200px;display:flex;align-items:center;justify-content:center;gap:22px;font-weight:900;font-size:34px;color:var(--blue)}
.center-head::before,.center-head::after{content:"";width:60px;height:3px;background:var(--green)}
.center-head .accent{color:var(--green)}
/* reviews */
.reviews-list{left:96px;top:1790px;width:1008px;display:flex;justify-content:space-between}
.review{width:320px;height:240px;background:var(--white);border-radius:6px;box-shadow:0 4px 18px rgba(20,40,80,.1);padding:24px;position:relative}
.review p{font-size:13px;color:var(--muted);line-height:1.55;height:100px}
.stars{color:#f5b400;font-size:18px;letter-spacing:2px;text-align:right;margin:6px 0 10px}
.reviewer{display:flex;align-items:center;gap:12px;border-top:1px solid var(--line);padding-top:14px}
.avatar{width:40px;height:40px;border-radius:50%;background:#c8d0d9}
.reviewer b{display:block;font-size:13px;color:var(--blue)}
.reviewer small{font-size:11px;color:var(--muted)}
.arrow{width:36px;height:36px;border-radius:50%;background:var(--white);box-shadow:0 2px 8px rgba(0,0,0,.15);display:flex;align-items:center;justify-content:center}
.btn-view{left:540px;width:120px;height:40px;border-radius:20px;background:var(--green);color:var(--white);font-weight:700;font-size:13px;display:flex;align-items:center;justify-content:center}
/* why */
.why-list{left:88px;top:2392px;width:1024px;display:flex;justify-content:space-between}
.why-card{width:320px;height:310px;border-radius:4px;position:relative;overflow:hidden;padding:24px;display:flex;flex-direction:column;justify-content:flex-end;align-items:center;text-align:center}
.why-card.photo-tech{background:linear-gradient(160deg,#123a73,#0b1f45 70%)}
.why-card.plain{background:var(--navy);justify-content:center}
.why-card.photo-people{background:linear-gradient(160deg,#c9a27a,#6b5440 50%,#1a2238)}
.why-icon{width:44px;height:44px;border-radius:50%;background:var(--blue);display:flex;align-items:center;justify-content:center;margin-bottom:14px}
.why-card h3{font-weight:900;font-size:20px;line-height:1.2;color:var(--green);margin-bottom:10px}
.why-card p{font-size:13px;color:#d7dde7;line-height:1.55}
/* articles */
.article-list{left:88px;top:2920px;width:1024px;display:flex;justify-content:space-between}
.article{width:320px}
.thumb{height:190px;border-radius:4px}
.thumb.t1{background:linear-gradient(135deg,#d2d8de,#8c99a6)}
.thumb.t2{background:linear-gradient(135deg,#e5e9ec,#b7c2cc)}
.thumb.t3{background:linear-gradient(135deg,#2d4d7a,#b64a4a)}
.tag{display:inline-block;margin:12px 0 8px;padding:3px 10px;font-size:11px;font-weight:700;color:var(--white);border-radius:2px;background:var(--blue)}
.tag.green{background:var(--green)}
.article h4{font-size:16px;font-weight:900;color:var(--ink);line-height:1.3;text-transform:uppercase}
/* footer */
.site-footer{left:0;top:3320px;width:1200px;height:412px;background:var(--blue);color:var(--white)}
.news-title{left:88px;top:3358px;font-size:13px;font-weight:700;color:var(--green)}
.news-form{left:88px;top:3384px;display:flex}
.news-input{width:310px;height:40px;background:var(--white);border-radius:3px 0 0 3px;color:var(--muted);font-size:12px;display:flex;align-items:center;padding:0 14px}
.news-btn{width:150px;height:40px;background:var(--green);color:var(--white);border-radius:0 3px 3px 0;font-weight:700;font-size:13px;display:flex;align-items:center;justify-content:center}
.pay-cards{left:796px;top:3384px;display:flex;gap:12px}
.pay{width:76px;height:46px;background:var(--white);border-radius:4px;color:var(--blue-dark);font-weight:700;font-size:12px;display:flex;align-items:center;justify-content:center}
.footer-rule{left:88px;top:3470px;width:1024px;height:1px;background:rgba(255,255,255,.3)}
.footer-col{top:3500px;font-size:13px;line-height:1.9;color:var(--footer-text)}
.footer-col h5{font-size:14px;font-weight:700;color:var(--green);margin-bottom:8px;letter-spacing:.5px}
.contact-line{display:flex;align-items:flex-start;gap:10px}
.contact-line svg{flex:none;margin-top:6px}
.copyright{left:0;top:3696px;width:1200px;text-align:center;font-size:12px;color:var(--footer-text)}
</style>
</head>
<body>

<section class="hero abs">
  <svg class="hero-wave abs" width="1200" height="620" viewBox="0 0 1200 620" aria-hidden="true">
    <path d="M560 0 H1200 V300 C1080 180 900 120 760 90 C660 70 600 40 560 0Z" fill="#7cc242"/>
    <path d="M640 0 H1200 V200 C1090 110 920 80 790 60 C720 48 670 26 640 0Z" fill="#8fd050" opacity=".6"/>
  </svg>
  <div class="hero-devices abs" role="img" aria-label="Desktop, tablet and phone screens showing a credit score dashboard"></div>
  <h1 class="hero-title abs">CHECK YOUR CREDIT SCORE<br>WITHIN SECONDS</h1>
  <form class="signup-card abs">
    <h2>GET STARTED NOW</h2>
    <div class="field">ID Number</div>
    <div class="field">First Name</div>
    <div class="field">Last Name</div>
    <div class="field">Primary Email</div>
    <div class="field">Mobile Number</div>
    <div class="agree"><span></span>I agree with the terms and conditions</div>
    <div class="btn-submit">SUBMIT MY SCORE</div>
  </form>
</section>
<p class="signup-note abs">By signing up and agreeing with the terms you authorise BrightLedgerView.co.za to request your credit report from the bureaus and display it within the site.</p>

<header class="site-header abs">
  <div class="brand abs"><span class="brand-dot"></span><span class="brand-name">BrightLedgerView</span></div>
  <nav class="main-nav abs"><span class="active">HOME</span><span>ARTICLES</span><span>ABOUT</span><span>CONTACT</span></nav>
  <div class="btn-login abs">LOGIN</div>
</header>

<div class="benefits abs">
  <div class="benefit"><svg class="tick" viewBox="0 0 32 32"><circle cx="16" cy="16" r="16" fill="#7cc242"/><path d="M9 16l5 5 9-10" stroke="#fff" stroke-width="3" fill="none"/></svg>See your most recent credit score</div>
  <div class="benefit"><svg class="tick" viewBox="0 0 32 32"><circle cx="16" cy="16" r="16" fill="#7cc242"/><path d="M9 16l5 5 9-10" stroke="#fff" stroke-width="3" fill="none"/></svg>Get access to your full credit profile</div>
  <div class="benefit"><svg class="tick" viewBox="0 0 32 32"><circle cx="16" cy="16" r="16" fill="#7cc242"/><path d="M9 16l5 5 9-10" stroke="#fff" stroke-width="3" fill="none"/></svg>See who has been looking at your profile</div>
  <div class="benefit"><svg class="tick" viewBox="0 0 32 32"><circle cx="16" cy="16" r="16" fill="#7cc242"/><path d="M9 16l5 5 9-10" stroke="#fff" stroke-width="3" fill="none"/></svg>See if you have any adverse or Blacklistings</div>
</div>
<div class="rule abs"></div>

<div class="about-ring abs"></div>
<div class="about-photo abs" role="img" aria-label="Person checking finances on a laptop"></div>
<div class="about-text abs">
  <h2 class="section-title">ABOUT US</h2>
  <p>BrightLedgerView.co.za (BLV) is a web based platform that enables credit active consumers to get direct access to their credit scores and profiles in an easy to understand and interactive online report.</p>
  <p>BLV launched in November 2015 and has since helped thousands of South Africans get access to their credit reports, many people becoming regular users on our platform.</p>
  <p>For investor and media enquiries email <a>info@brightledgerview.co.za</a></p>
</div>

<section class="features abs"></section>
<div class="features-photo abs" role="img" aria-label="Hands typing on a laptop keyboard"></div>
<div class="features-title abs"><h2 class="section-title">SYSTEM FEATURES</h2></div>
<div class="feature-col abs" style="left:88px">
  <div class="feature"><span class="f-icon"><svg width="20" height="20" viewBox="0 0 20 20"><rect x="3" y="4" width="14" height="12" rx="2" fill="none" stroke="#fff" stroke-width="2"/></svg></span>Budget tool - easily create a budget</div>
  <div class="feature"><span class="f-icon"><svg width="20" height="20" viewBox="0 0 20 20"><path d="M4 3h9l3 3v11H4z" fill="none" stroke="#fff" stroke-width="2"/></svg></span>Improve your credit score eBook</div>
  <div class="feature"><span class="f-icon"><svg width="20" height="20" viewBox="0 0 20 20"><path d="M3 4h14v12H3zM3 9h14M9 4v12" fill="none" stroke="#fff" stroke-width="2"/></svg></span>Personal Budgeting Spreadsheet</div>
  <div class="feature"><span class="f-icon"><svg width="20" height="20" viewBox="0 0 20 20"><path d="M10 3l7 13H3z" fill="none" stroke="#fff" stroke-width="2"/></svg></span>Dispute generator - easily manage disputes</div>
</div>
<div class="feature-col abs" style="left:360px">
  <div class="feature"><span class="f-icon"><svg width="20" height="20" viewBox="0 0 20 20"><path d="M4 11a6 6 0 0112 0v4h-3v-4M4 11v4h3v-4" fill="none" stroke="#fff" stroke-width="2"/></svg></span>Dedicated 24/7 Support</div>
  <div class="feature"><span class="f-icon"><svg width="20" height="20" viewBox="0 0 20 20"><path d="M7 5l8 5-8 5z" fill="#fff"/></svg></span>Personal Finance Video Tutorials</div>
  <div class="feature"><span class="f-icon"><svg width="20" height="20" viewBox="0 0 20 20"><circle cx="10" cy="10" r="7" fill="none" stroke="#fff" stroke-width="2"/><path d="M8 7l5 3-5 3z" fill="#fff"/></svg></span>Perfect score video course</div>
</div>

<h2 class="center-head abs" style="top:1700px">USER REVIEWS <span class="accent">VERIFIED REVIEWS</span></h2>
<div class="arrow abs" style="left:40px;top:1888px"><svg width="12" height="12" viewBox="0 0 12 12"><path d="M8 1L3 6l5 5" stroke="#333" stroke-width="2" fill="none"/></svg></div>
<div class="arrow abs" style="left:1124px;top:1888px"><svg width="12" height="12" viewBox="0 0 12 12"><path d="M4 1l5 5-5 5" stroke="#333" stroke-width="2" fill="none"/></svg></div>
<div class="reviews-list abs">
  <article class="review">
    <p>The credit report is easy to use, informative and accurate to the date. Helps me to manage my finances well and keep my score growing.</p>
    <div class="stars">★★★★★</div>
    <div class="reviewer"><span class="avatar"></span><div><b>Carla Jansen</b><small>30 Sep · 28 reviews</small></div></div>
  </article>
  <article class="review">
    <p>Their customer support team has been very impressive. The tools and knowledge they shared were of great practical use.</p>
    <div class="stars">★★★★★</div>
    <div class="reviewer"><span class="avatar"></span><div><b>Thandi Mokoena</b><small>30 Sep · 7 reviews</small></div></div>
  </article>
  <article class="review">
    <p>The credit report is easy to use and efficient, and it was very quick to join. Also very helpful.</p>
    <div class="stars">★★★★★</div>
    <div class="reviewer"><span class="avatar"></span><div><b>Pieter Naidoo</b><small>30 Sep · 1 review</small></div></div>
  </article>
</div>
<div class="btn-view abs" style="top:2124px">VIEW ALL</div>

<h2 class="center-head abs" style="top:2318px">WHY GET YOUR SCORE FROM US?</h2>
<div class="why-list abs">
  <div class="why-card photo-tech" role="img" aria-label="Digital security lock on a circuit background">
    <div class="why-icon"><svg width="20" height="20" viewBox="0 0 20 20"><rect x="4" y="9" width="12" height="8" rx="1" fill="#fff"/><path d="M7 9V6a3 3 0 016 0v3" stroke="#fff" stroke-width="2" fill="none"/></svg></div>
    <h3>WE DON'T ABUSE YOUR<br>PERSONAL INFORMATION</h3>
  </div>
  <div class="why-card plain">
    <div class="why-icon"><svg width="20" height="20" viewBox="0 0 20 20"><path d="M5 3h10v14H5zM8 7h4M8 10h4M8 13h4" stroke="#fff" stroke-width="2" fill="none"/></svg></div>
    <h3>OUR REPORT IS SUPER<br>EASY TO UNDERSTAND</h3>
    <p>Our credit report is one of the easiest reports to understand. The report is clearly laid out and you will see immediately if you can apply for finance, if you are blacklisted, and where you can improve.</p>
  </div>
  <div class="why-card photo-people" role="img" aria-label="Smiling customer holding a phone">
    <div class="why-icon"><svg width="20" height="20" viewBox="0 0 20 20"><circle cx="10" cy="7" r="3" fill="#fff"/><path d="M4 17a6 6 0 0112 0z" fill="#fff"/></svg></div>
    <h3>300,000 + SOUTH AFRICANS<br>HAVE TRUSTED US</h3>
  </div>
</div>

<h2 class="center-head abs" style="top:2848px">ARTICLES</h2>
<div class="article-list abs">
  <article class="article">
    <div class="thumb t1" role="img" aria-label="Presenter discussing credit score changes"></div>
    <span class="tag">Credit Report Tips &amp; Advice</span>
    <h4>Massive credit score changes coming to South Africa</h4>
  </article>
  <article class="article">
    <div class="thumb t2" role="img" aria-label="Presenter explaining a loan calculator"></div>
    <span class="tag green">Credit Education</span>
    <h4>Personal loan repayment calculator</h4>
  </article>
  <article class="article">
    <div class="thumb t3" role="img" aria-label="Identity theft warning graphic"></div>
    <span class="tag">Credit Report Tips &amp; Advice</span>
    <h4>Identity theft in South Africa is up 337%</h4>
  </article>
</div>
<div class="btn-view abs" style="top:3218px">VIEW ALL</div>

<footer class="site-footer abs"></footer>
<div class="news-title abs">SIGN UP TO KNOW LATEST FROM US</div>
<div class="news-form abs"><div class="news-input">Enter your email address here</div><div class="news-btn">SUBSCRIBE NOW</div></div>
<div class="pay-cards abs"><div class="pay">Zentrova</div><div class="pay">Plumora</div><div class="pay">Vastlee</div></div>
<div class="footer-rule abs"></div>
<div class="footer-col abs" style="left:88px">
  <h5>CONTACT INFO</h5>
  <div class="contact-line"><svg width="14" height="14" viewBox="0 0 14 14"><path d="M7 1a4 4 0 014 4c0 3-4 8-4 8S3 8 3 5a4 4 0 014-4z" fill="#7cc242"/></svg><span>14 Harbour Lane, Seaview,<br>Cape Town, 8001</span></div>
  <div class="contact-line"><svg width="14" height="14" viewBox="0 0 14 14"><path d="M3 1l3 3-2 2a8 8 0 004 4l2-2 3 3-2 2C6 13 1 8 1 3z" fill="#7cc242"/></svg><span>(021) 555-0142</span></div>
  <div class="contact-line"><svg width="14" height="14" viewBox="0 0 14 14"><rect x="1" y="3" width="12" height="8" fill="#7cc242"/><path d="M1 3l6 5 6-5" stroke="#1d5cb8" fill="none"/></svg><span>support@brightledgerview.co.za</span></div>
</div>
<div class="footer-col abs" style="left:420px">
  <h5>TERMS</h5>
  <div>General Terms of use</div><div>Exclusion of Liability</div><div>Security Policy</div><div>Privacy Policy</div>
</div>
<div class="footer-col abs" style="left:680px">
  <h5>PURCHASE</h5>
  <div>Delivery Policy</div><div>Data Policy</div><div>Refund Policy</div><div>Charges and Fees</div>
</div>
<div class="footer-col abs" style="left:940px">
  <h5>QUICK LINKS</h5>
  <div>Articles</div><div>Contact Us</div><div>Login</div>
</div>
<div class="copyright abs">Copyright © 2022 by Bright Ledger View. All Rights Reserved</div>

</body>
</html>
```